Electrical and Audio Visual Business Card Design

We need a business card design for our company called T.O.K.E.N (Tovin's Ohm Kinetic & Electrical Networks PtyLtd).
We provide Electrical Services as well as Audio Visual demands.
Services provided:
Electrical repairs
Additions
Extensions
Audio Visual solutions
Data
Smoke alarms
TV antennas
Automation
Updates

Also looking for a company logo. Uniforms are black if this helps.

Industry/Entity Type

Business

Contact Information for Business Card

T.O.K.E.N Pty Ltd
Martin Okelbury
58 Tallow Rd,
Wingham, 2817
mokelbury@token-example.net.au

Logo Text

T.O.K.E.N.

Requirements
Must have
• Please can we have a double sided card. Showing our services on the back. Can I also have the number 0417395286. Can we also change email address to mokelbury@token-example.net.au

```html
<!DOCTYPE html>
<html lang="en">
<head>
<meta charset="utf-8">
<title>T.O.K.E.N Business Card</title>
<link rel="stylesheet" href="https://fonts.googleapis.com/css2?family=Michroma&display=swap">
<style>
  :root {
    --backdrop: #2b2b2b;
    --card-dark: #1f1f1f;
    --card-light: #f4f4f4;
    --brand-blue: #1e8fe0;
    --text-light: #e6e6e6;
    --text-dark: #222222;
    --ghost-grey: #d6d6d6;
    --rule-grey: #9a9a9a;
  }
  * { margin: 0; padding: 0; box-sizing: border-box; }
  html, body {
    width: 1200px; height: 900px; overflow: hidden;
    background: var(--backdrop);
    font-family: "Michroma", sans-serif;
  }
  .canvas { position: relative; width: 1200px; height: 900px; }

  .card {
    position: absolute; width: 520px; height: 300px; overflow: hidden;
    box-shadow: 0 14px 30px rgba(0,0,0,0.55);
  }

  /* Back of card: services */
  .card-back { left: 50px; top: 330px; background: var(--card-light); }
  .ghost-name {
    position: absolute; left: 10px; bottom: -10px;
    font-size: 70px; letter-spacing: 0; color: var(--ghost-grey);
    white-space: nowrap; line-height: 1;
  }
  .services-title {
    position: absolute; left: 0; right: 0; top: 62px; text-align: center;
    font-size: 12px; font-weight: 400; color: var(--brand-blue); letter-spacing: 0.5px;
  }
  .services-title span {
    display: inline-block; padding-bottom: 5px; border-bottom: 1px solid var(--rule-grey);
  }
  .service-list { position: absolute; list-style: none; font-size: 10.5px; color: var(--text-dark); line-height: 15px; }
  .service-list.col-left { left: 60px; top: 96px; }
  .service-list.col-right { left: 300px; top: 142px; }
  .service-list li { display: flex; align-items: center; gap: 6px; }
  .service-list svg { width: 9px; height: 9px; fill: var(--brand-blue); flex: none; }

  /* Front of card: identity */
  .card-front { left: 630px; top: 230px; background: var(--card-dark); }
  .brand { position: absolute; right: 34px; top: 58px; text-align: right; }
  .brand-name { font-size: 52px; font-weight: 400; color: var(--brand-blue); letter-spacing: 3px; line-height: 1; }
  .brand-full {
    margin-top: 8px; font-size: 9px; color: var(--text-light); line-height: 12px; letter-spacing: 0.2px;
  }
  .contact { position: absolute; right: 34px; top: 172px; text-align: right; }
  .contact-name {
    display: inline-block; font-size: 13px; color: var(--brand-blue);
    padding-bottom: 5px; border-bottom: 1px solid var(--rule-grey);
  }
  .contact-line { margin-top: 10px; font-size: 10px; color: var(--text-light); white-space: nowrap; }
  .contact-line + .contact-line { margin-top: 6px; }
  .contact-line .email { color: var(--brand-blue); }
</style>
</head>
<body>
<main class="canvas">

  <section class="card card-back" aria-label="Card back: services">
    <div class="ghost-name" aria-hidden="true">T.O.K.E.N</div>
    <h2 class="services-title"><span>SERVICES PROVIDED:</span></h2>
    <ul class="service-list col-left">
      <li><svg viewBox="0 0 10 10"><polygon points="5,0 6.2,3.6 10,3.8 7,6.1 8.1,10 5,7.7 1.9,10 3,6.1 0,3.8 3.8,3.6"/></svg>ELECTRICAL REPAIRS</li>
      <li><svg viewBox="0 0 10 10"><polygon points="5,0 6.2,3.6 10,3.8 7,6.1 8.1,10 5,7.7 1.9,10 3,6.1 0,3.8 3.8,3.6"/></svg>ADDITIONS</li>
      <li><svg viewBox="0 0 10 10"><polygon points="5,0 6.2,3.6 10,3.8 7,6.1 8.1,10 5,7.7 1.9,10 3,6.1 0,3.8 3.8,3.6"/></svg>EXTENSIONS</li>
      <li><svg viewBox="0 0 10 10"><polygon points="5,0 6.2,3.6 10,3.8 7,6.1 8.1,10 5,7.7 1.9,10 3,6.1 0,3.8 3.8,3.6"/></svg>AUDIO VISUAL SOLUTIONS</li>
    </ul>
    <ul class="service-list col-right">
      <li><svg viewBox="0 0 10 10"><polygon points="5,0 6.2,3.6 10,3.8 7,6.1 8.1,10 5,7.7 1.9,10 3,6.1 0,3.8 3.8,3.6"/></svg>DATA</li>
      <li><svg viewBox="0 0 10 10"><polygon points="5,0 6.2,3.6 10,3.8 7,6.1 8.1,10 5,7.7 1.9,10 3,6.1 0,3.8 3.8,3.6"/></svg>SMOKE ALARMS</li>
      <li><svg viewBox="0 0 10 10"><polygon points="5,0 6.2,3.6 10,3.8 7,6.1 8.1,10 5,7.7 1.9,10 3,6.1 0,3.8 3.8,3.6"/></svg>TV ANTENNAS</li>
      <li><svg viewBox="0 0 10 10"><polygon points="5,0 6.2,3.6 10,3.8 7,6.1 8.1,10 5,7.7 1.9,10 3,6.1 0,3.8 3.8,3.6"/></svg>AUTOMATION</li>
      <li><svg viewBox="0 0 10 10"><polygon points="5,0 6.2,3.6 10,3.8 7,6.1 8.1,10 5,7.7 1.9,10 3,6.1 0,3.8 3.8,3.6"/></svg>UPDATES</li>
    </ul>
  </section>

  <section class="card card-front" aria-label="Card front: contact">
    <div class="brand">
      <h1 class="brand-name">T.O.K.E.N</h1>
      <p class="brand-full">TOVIN'S OHM KINETIC &amp; ELECTRICAL NETWORKS<br>PTY LTD</p>
    </div>
    <div class="contact">
      <p class="contact-name">MARTIN OKELBURY</p>
      <p class="contact-line">58 TALLOW RD, WINGHAM, 2817 &nbsp;//&nbsp; 0417395286</p>
      <p class="contact-line"><span class="email">MOKELBURY@TOKEN-EXAMPLE.NET.AU</span></p>
    </div>
  </section>

</main>
</body>
</html>
```